iron deficiency anemia - educational reference paper

looking for an educational paper/poster 8x11 or no larger than 11x14 that lists the most common foods with pictures and limited words a super rough outline attached - I wrote the words of the pictures (but would like to have the actual pictures of these items) I would like in roughly the same order
for the pictures for fatigue, headache....can be drawings or cartoons
double sided or single sided (which ever fits) see attached for categories (3 of them)

Target Market(s)

educational for people with limited education - thus not much wording

Requirements
Must have
• pictures, simple design

```html
<!DOCTYPE html>
<html lang="en">
<head>
<meta charset="utf-8">
<title>Iron Deficiency Anemia</title>
<link rel="stylesheet" href="https://fonts.googleapis.com/css2?family=Montserrat:wght@400;600;700;800&family=Playfair+Display:wght@900&display=swap">
<style>
  :root {
    --red: #8e1414;
    --ink: #2a2a2a;
    --paper: #f4f4f4;
    --wash: #e4e4e4;
    --band: #5b5b5b;
    --white: #ffffff;
  }
  * { margin: 0; padding: 0; box-sizing: border-box; }
  html, body { width: 927px; height: 1200px; overflow: hidden; background: var(--paper); }
  .poster {
    position: relative; width: 927px; height: 1200px; overflow: hidden;
    background: var(--paper); font-family: "Montserrat", sans-serif; color: var(--ink);
  }
  .backdrop { position: absolute; inset: 0; }
  .top-band { position: absolute; left: 0; top: 0; width: 100%; height: 20px; background: var(--red); }

  .kicker {
    position: absolute; top: 56px; left: 0; width: 100%;
    display: flex; justify-content: center; align-items: center; gap: 18px;
    font-size: 19px; font-weight: 400; letter-spacing: 13px; color: var(--ink);
  }
  .kicker::before, .kicker::after { content: ""; width: 50px; height: 1.5px; background: var(--ink); }
  .kicker::before { margin-right: 6px; }
  .title {
    position: absolute; top: 74px; left: 0; width: 100%; text-align: center;
    font-family: "Playfair Display", serif; font-weight: 900; font-size: 152px;
    line-height: 1.1; letter-spacing: 2px; color: var(--red);
    text-shadow: 2px 2px 0 var(--white), 4px 4px 0 var(--ink);
  }

  .foods-frame {
    position: absolute; left: 113px; top: 282px; width: 708px; height: 274px;
    border: 1.5px solid var(--ink); border-radius: 16px;
  }
  .foods-heading { position: absolute; top: 269px; left: 0; width: 100%; text-align: center; }
  .foods-heading span {
    display: inline-block; padding: 0 22px; background: var(--paper);
    font-size: 16.5px; font-weight: 700; letter-spacing: 0.2px; color: var(--ink);
  }
  .foods-list {
    position: absolute; left: 201px; top: 326px; width: 530px;
    font-size: 14px; line-height: 20.8px; color: var(--ink);
  }
  .foods-list .row { display: block; text-align: justify; text-align-last: justify; white-space: nowrap; }
  .foods-list .row.last { text-align: center; text-align-last: center; word-spacing: 6px; }
  .food-photo {
    position: absolute; width: 156px; height: 150px; border-radius: 50%;
    background: var(--paper); border: 1.5px solid var(--ink); padding: 7px;
  }
  .food-photo .fill { width: 100%; height: 100%; border-radius: 50%; }
  .food-photo.livestock { left: 36px; top: 346px; }
  .food-photo.livestock .fill { background: linear-gradient(160deg, #3f4a3a 0%, #d9ddd6 45%, #6f8a4c 100%); }
  .food-photo.legumes { left: 741px; top: 346px; }
  .food-photo.legumes .fill { background: radial-gradient(circle at 65% 55%, #7fa94a 0%, #c9ad72 45%, #b38f55 100%); }

  .symptoms-banner { position: absolute; left: 338px; top: 620px; width: 262px; height: 56px; }
  .symptoms-banner .label {
    position: absolute; inset: 0; display: flex; align-items: center; justify-content: center;
    font-size: 18.5px; font-weight: 800; color: var(--white); letter-spacing: 0.2px;
  }
  .timeline { position: absolute; left: 0; top: 686px; width: 100%; height: 3px; background: var(--ink); }
  .step { position: absolute; top: 677px; width: 128px; margin-left: -64px; display: flex; flex-direction: column; align-items: center; }
  .step .num {
    width: 21px; height: 21px; border-radius: 50%; background: var(--red); border: 2px solid var(--white);
    box-shadow: 0 0 0 1px var(--ink); color: var(--white); font-size: 10px; font-weight: 700;
    display: flex; align-items: center; justify-content: center;
  }
  .step .stem { width: 2.5px; height: 30px; background: var(--ink); margin-top: 6px; }
  .step .pill {
    margin-top: 12px; width: 128px; height: 44px; border-radius: 14px; background: var(--red);
    color: var(--white); font-size: 11.5px; font-weight: 700; text-align: center; line-height: 1.15;
    display: flex; align-items: center; justify-content: center;
  }

  .signs-heading {
    position: absolute; top: 880px; left: 0; width: 100%;
    display: flex; justify-content: center; align-items: center; gap: 22px;
    font-size: 35px; font-weight: 800; color: var(--red); letter-spacing: 0.3px;
  }
  .signs-heading::before, .signs-heading::after { content: ""; width: 113px; height: 3px; background: var(--ink); border-radius: 2px; }
  .bottom-band { position: absolute; left: 0; top: 1085px; width: 100%; height: 115px; background: var(--band); }
  .sign-photo {
    position: absolute; top: 967px; width: 212px; height: 204px; border-radius: 50%;
    background: var(--wash); padding: 13px;
  }
  .sign-photo .fill { width: 100%; height: 100%; border-radius: 50%; }
  .sign-photo.pale-palm { left: 75px; }
  .sign-photo.pale-palm .fill { background: linear-gradient(120deg, #6f8c96 0%, #d9b7a3 50%, #c99a86 100%); }
  .sign-photo.pale-eyelid { left: 357px; }
  .sign-photo.pale-eyelid .fill { background: linear-gradient(180deg, #8b8f94 0%, #e9c7b6 40%, #e8b9a6 100%); }
  .sign-photo.pale-tongue { left: 643px; }
  .sign-photo.pale-tongue .fill { background: radial-gradient(circle at 55% 60%, #d8aeaa 0%, #c89a94 45%, #7d6a62 100%); }
</style>
</head>
<body>
<main class="poster">
  <svg class="backdrop" width="927" height="1200" viewBox="0 0 927 1200" aria-hidden="true">
    <path d="M0 800 C 90 660, 170 560, 330 520 C 520 470, 640 560, 720 540 C 770 525, 740 380, 780 260 C 810 180, 880 165, 927 150 L 927 1200 L 0 1200 Z" fill="#e6e6e6"/>
  </svg>
  <div class="top-band"></div>

  <p class="kicker">IRON DEFICIENCY</p>
  <h1 class="title">ANEMIA</h1>

  <section class="foods">
    <div class="foods-frame"></div>
    <h2 class="foods-heading"><span>COMMON FOODS IN YOUR COMMUNITY</span></h2>
    <p class="foods-list">
      <span class="row">Sheep/lamb goose whale winged bean rice bran white bean</span>
      <span class="row">pig/pork kidney bean cowpea black bean mung bean natto</span>
      <span class="row">teff amaranth yardlong bean chili/pink bean lentil yellow</span>
      <span class="row">bean duck lima bean chicken clams pumpkin seen squab</span>
      <span class="row">pigeon pea fava bean sesame seed aduzki bean cranberry</span>
      <span class="row">bean masa split peas cuttlefish bear sunflower seed bagel</span>
      <span class="row">sardines ckickpeas shrimp spinach beet brussle sprouts egg</span>
      <span class="row">collard greens muschrooms nuts potatoe tortilla turkey</span>
      <span class="row last">blackberry broccoli carrot califlower halibut tomatoe</span>
    </p>
    <div class="food-photo livestock"><div class="fill" role="img" aria-label="Photo of a dairy cow standing in a green field"></div></div>
    <div class="food-photo legumes"><div class="fill" role="img" aria-label="Photo of soybeans with green pods and leaf"></div></div>
  </section>

  <section class="symptoms">
    <div class="symptoms-banner">
      <svg width="262" height="56" viewBox="0 0 262 56" aria-hidden="true">
        <polygon points="10,0 252,0 262,22 262,34 252,56 10,56 0,34 0,22" fill="#3a3a3a"/>
        <polygon points="14,6 248,6 256,22 250,28 256,34 248,48 14,48 6,34 12,28 6,22" fill="#8e1414"/>
      </svg>
      <h2 class="label">SYMPTOMS OF ANEMIA</h2>
    </div>
    <div class="timeline"></div>
    <div class="step" style="left:142px"><span class="num">1</span><span class="stem"></span><span class="pill">FATIGUE</span></div>
    <div class="step" style="left:305px"><span class="num">2</span><span class="stem"></span><span class="pill">HEADACHE</span></div>
    <div class="step" style="left:469px"><span class="num">3</span><span class="stem"></span><span class="pill">DIZZINESS</span></div>
    <div class="step" style="left:629px"><span class="num">4</span><span class="stem"></span><span class="pill">BLURRY VISION</span></div>
    <div class="step" style="left:789px"><span class="num">5</span><span class="stem"></span><span class="pill">MUSCLE<br>WEAKNESS</span></div>
  </section>

  <section class="signs">
    <h2 class="signs-heading">SIGNS OF ANEMIA</h2>
    <div class="bottom-band"></div>
    <div class="sign-photo pale-palm"><div class="fill" role="img" aria-label="Photo of a pale palm of the hand"></div></div>
    <div class="sign-photo pale-eyelid"><div class="fill" role="img" aria-label="Close-up photo of a pale lower eyelid"></div></div>
    <div class="sign-photo pale-tongue"><div class="fill" role="img" aria-label="Close-up photo of a pale, smooth tongue"></div></div>
  </section>
</main>
</body>
</html>
```